Thank You Card

I'm looking for a thank you card design using our logo and other graphics. We are an essential business and our employees (Electricians) have done an incredible job staying healthy and safe during the COVID-19 pandemic, I want to send each a thank you card.

```html
<!DOCTYPE html>
<html lang="en">
<head>
<meta charset="utf-8">
<title>Thank You Card</title>
<link rel="stylesheet" href="https://fonts.googleapis.com/css2?family=Roboto:ital,wght@0,500;1,400;1,500&family=Yellowtail&display=swap">
<style>
  :root {
    --page: #ffffff;
    --ink-navy: #2b3690;
    --frame-red: #e3242b;
    --glow-gold: #ffd23a;
    --glow-amber: #f7a21b;
    --glow-orange: #e2561a;
    --glow-deep: #8a1f0a;
    --night: #0a0604;
    --cream: #fbf3df;
    --lettering-shadow: #7a3a08;
  }
  * { box-sizing: border-box; margin: 0; padding: 0; }
  html, body { width: 1200px; height: 675px; overflow: hidden; background: var(--page); }
  .canvas { position: relative; width: 1200px; height: 675px; background: var(--page); }

  .card-front {
    position: absolute; left: 21px; top: 23px; width: 487px; height: 630px;
    border: 1px solid #3a2a10; overflow: hidden;
  }
  .front-light {
    position: absolute; inset: 0;
    background:
      radial-gradient(circle at 8% 52%, rgba(255,252,225,1) 0, rgba(255,225,100,0.8) 14%, transparent 40%),
      radial-gradient(circle at 85% 28%, rgba(255,240,180,0.85) 0, transparent 26%),
      radial-gradient(circle at 90% 62%, rgba(255,220,90,0.8) 0, transparent 18%),
      radial-gradient(circle at 45% 15%, var(--glow-orange) 0, transparent 38%),
      radial-gradient(circle at 30% 85%, rgba(255,200,40,0.85) 0, transparent 32%),
      radial-gradient(circle at 95% 95%, var(--night) 0, transparent 40%),
      radial-gradient(circle at 0% 0%, rgba(20,10,0,0.9) 0, transparent 20%),
      linear-gradient(160deg, var(--glow-amber) 0%, var(--glow-orange) 45%, var(--glow-deep) 78%, var(--night) 100%);
  }
  .front-greeting {
    position: absolute; left: 50px; top: 180px; width: 420px;
    font-family: "Yellowtail", cursive; font-weight: 400;
    color: var(--cream); line-height: 0.82; text-align: left;
    transform: rotate(-6deg); transform-origin: left top;
    text-shadow: 2px 3px 0 var(--lettering-shadow), 0 0 14px rgba(90,40,0,0.6);
  }
  .front-greeting .word-thank { display: block; font-size: 150px; }
  .front-greeting .word-you { display: block; font-size: 150px; margin-left: 70px; }

  .card-inside {
    position: absolute; left: 547px; top: 100px; width: 631px; height: 487px;
    border: 1px solid #3a2a10;
    background:
      radial-gradient(circle at 5% 10%, rgba(255,245,180,0.95) 0, transparent 30%),
      radial-gradient(circle at 60% 98%, rgba(255,230,120,0.9) 0, transparent 30%),
      radial-gradient(circle at 98% 90%, rgba(255,240,200,0.8) 0, transparent 20%),
      linear-gradient(135deg, var(--glow-gold) 0%, var(--glow-amber) 30%, var(--glow-orange) 55%, var(--glow-deep) 80%, var(--night) 100%);
  }
  .inside-panel {
    position: absolute; left: 23px; top: 22px; right: 23px; bottom: 23px;
    background: var(--page);
  }
  .inside-frame {
    position: absolute; inset: 5px 4px 4px 5px;
    border: 2px solid var(--frame-red);
  }

  .message-column {
    position: absolute; left: 40px; top: 0; width: 255px;
    text-align: center; font-family: "Roboto", sans-serif; color: var(--ink-navy);
  }
  .company-name {
    margin-top: 40px; font-weight: 500; font-style: normal; color: var(--ink-navy);
    line-height: 1.05; letter-spacing: 0.5px;
  }
  .company-name .name-main { display: block; font-size: 30px; }
  .company-name .name-sub { display: block; font-size: 15px; letter-spacing: 3px; margin-top: 4px; }

  .message {
    margin-top: 34px; font-style: italic; font-weight: 400; font-size: 16px; line-height: 27px;
  }
  .message .strong { font-weight: 500; }
  .divider { display: block; margin: 8px auto 0; }
</style>
</head>
<body>
  <main class="canvas">
    <section class="card-front">
      <div class="front-light" role="img" aria-label="Glowing golden and orange bokeh light background with sparkles"></div>
      <h1 class="front-greeting">
        <span class="word-thank">Thank</span>
        <span class="word-you">You</span>
      </h1>
    </section>

    <section class="card-inside" role="img" aria-label="Golden bokeh light border around the inside message">
      <div class="inside-panel">
        <div class="inside-frame">
          <div class="message-column">
            <p class="company-name">
              <span class="name-main">BRIGHTLINE</span>
              <span class="name-sub">ELECTRIC CO.</span>
            </p>
            <p class="message">
              The gift of your help<br>
              support in this critical<br>
              moment means more than<br>
              anything money can buy.<br>
              <span class="strong">We really appreciate all<br>
              that you've done and hope<br>
              this card provides a small<br>
              token of my gratitude.<br>
              Thanks!</span>
            </p>
            <svg class="divider" width="166" height="14" viewBox="0 0 166 14" aria-hidden="true">
              <line x1="1" y1="4" x2="165" y2="4" stroke="#2b3690" stroke-width="1"/>
              <rect x="80" y="6" width="5" height="5" transform="rotate(45 82.5 8.5)" fill="#2b3690"/>
            </svg>
          </div>
        </div>
      </div>
    </section>
  </main>
</body>
</html>
```